Harlow Finch Ltd. Recruitment Brochure

A 12pp A4 portrait brochure is required. It should have a contemporary and modern feel to it.

Please feel free to bring the flow chart to life with symbols that reflect the title of the stage in the flow chart.

Similarly the services that are offered should be brought to life.

See the attached brief for the detailed copy and brand colour details. I have also attached the logo and imagery to be used although we are open to additional / alternative imagery as long as it is royalty free and won't cost any additional money.

Target Market(s)

Small and medium sized businesses

Industry/Entity Type

Recruitment

Font styles to use
Serif
Sans Serif

Requirements
Must have
• See project brief.
Nice to have
• See project brief - bringing the flow chart and services aspects to life would be good.
Should not have
• See project brief.

```html
<!DOCTYPE html>
<html lang="en">
<head>
<meta charset="utf-8">
<title>Harlow Finch Ltd. – Our Process</title>
<link rel="stylesheet" href="https://fonts.googleapis.com/css2?family=Arimo:wght@400;700&display=swap">
<style>
  :root {
    --backdrop: #d1d2d4;
    --paper: #ffffff;
    --crimson: #7b1535;
    --slate: #6d6e70;
    --strip: #efefef;
    --ink: #231f20;
  }
  html, body { margin: 0; padding: 0; overflow: hidden; }
  body {
    width: 1200px; height: 1000px;
    background: var(--backdrop);
    position: relative;
    font-family: "Arimo", Arial, sans-serif;
  }
  .page {
    position: absolute; left: 293px; top: 61px;
    width: 613px; height: 860px;
    background: var(--paper);
  }
  .page__strip {
    position: absolute; left: 220px; top: 45px;
    width: 82px; height: 759px;
    background: var(--strip);
  }
  .page__footer-bar {
    position: absolute; left: 295px; top: 789px;
    width: 275px; height: 23px;
    background: var(--slate);
  }
  .stage { position: absolute; width: 240px; }
  .stage--left { left: 47px; }
  .stage--right { left: 305px; width: 244px; }
  .stage__number {
    position: absolute; left: 0; top: -8px;
    font-weight: 700; font-size: 62px; line-height: 1;
    color: var(--slate); letter-spacing: -2px;
  }
  .stage__bar {
    position: absolute; left: 37px; top: 0;
    width: 196px; height: 27px;
    background: var(--crimson);
    color: #fff; font-size: 13px; line-height: 27px;
    padding-left: 10px; box-sizing: border-box;
  }
  .stage__icon {
    position: absolute; right: 3px; top: 2px;
    width: 23px; height: 23px;
  }
  .stage__text {
    position: absolute; left: 0; top: 33px;
    width: 226px; margin: 0;
    font-size: 10.6px; line-height: 13.3px;
    color: var(--ink); text-indent: 56px;
  }
  .stage--right .stage__text { left: 3px; width: 234px; }
  .stage__text span { display: block; text-indent: 0; }
</style>
</head>
<body>
<main class="page" aria-label="Harlow Finch Ltd. recruitment process">
  <div class="page__strip"></div>

  <section class="stage stage--left" style="top:63px">
    <div class="stage__number">1</div>
    <h2 class="stage__bar" style="margin:0;font-weight:400">Understanding the brief
      <svg class="stage__icon" viewBox="0 0 24 24" fill="none" stroke="#fff" stroke-width="1.6"><path d="M7 21v-4a7 7 0 1 1 10-6l2 4h-2v3h-4v3"/><circle cx="13" cy="9" r="3.5"/><path d="M12 8a1 1 0 1 1 1.5 1v1"/></svg></h2>
    <p class="stage__text">we will meet with you to get a detailed understanding of both your organisation and the role including your vision and strategy. We will also undertake a job profile exercise to identify the key elements required from a perfect candidate. Finally, we will complete a project brief outlining all of the details for you to confirm.</p>
  </section>

  <section class="stage stage--right" style="top:63px">
    <div class="stage__number">2</div>
    <h2 class="stage__bar" style="margin:0;font-weight:400">Research
      <svg class="stage__icon" viewBox="0 0 24 24" fill="none" stroke="#fff" stroke-width="1.6"><rect x="3" y="3" width="15" height="12" rx="1"/><path d="M6 7h9M6 10h5"/><circle cx="15" cy="16" r="3.5"/><path d="M17.5 18.5 21 22"/></svg></h2>
    <p class="stage__text">once you have approved the project brief, we will undertake a detailed mapping exercise which will identify all of the possible companies that might currently employ your perfect candidate.<span>We will establish all of the potential candidates that exist within these companies, producing organograms where relevant to give you confidence we have undertaken a thorough search.</span></p>
  </section>

  <section class="stage stage--left" style="top:252px">
    <div class="stage__number">3</div>
    <h2 class="stage__bar" style="margin:0;font-weight:400">Approaches
      <svg class="stage__icon" viewBox="0 0 24 24" fill="none" stroke="#fff" stroke-width="1.8"><path d="M12 22V10M12 10 6 4M12 10l6-6M3 4h4v4M21 4h-4v4M9 15l3 3 3-3"/></svg></h2>
    <p class="stage__text">once you are happy with the list of prospective candidates, we will start making approaches and presenting them with the benefits of working for your organisation.<span>We will also undertake any initial screening of the candidate which establishes their location and remuneration package but also their skills, qualifications and experience to ensure they are suitable.</span></p>
  </section>

  <section class="stage stage--right" style="top:252px">
    <div class="stage__number">4</div>
    <h2 class="stage__bar" style="margin:0;font-weight:400">Assessment
      <svg class="stage__icon" viewBox="0 0 24 24" fill="none" stroke="#fff" stroke-width="1.6"><rect x="5" y="3" width="14" height="19" rx="1"/><rect x="9" y="1.5" width="6" height="3"/><path d="M9 8l6 6M15 8l-6 6M9 18l2 2 4-3"/></svg></h2>
    <p class="stage__text">successful candidates will then undergo a detailed assessment. We will refine all of the candidates to a list of suitable individuals to interview.<span>We will pick the best candidates for 1st interviews which will either be in person or via Vidlink.</span><span>Finally, those candidates who are successful at 1st interview will complete a psychometric profile to ensure they will be a good match for both the role and the organisation.</span></p>
  </section>

  <section class="stage stage--left" style="top:441px">
    <div class="stage__number">5</div>
    <h2 class="stage__bar" style="margin:0;font-weight:400">Shortlist meeting
      <svg class="stage__icon" viewBox="0 0 24 24" fill="none" stroke="#fff" stroke-width="1.6"><rect x="2" y="2" width="20" height="20"/><path d="M6 7h1M10 7h8M6 11h1M10 11h8M6 15h1M10 15h8M6 19h1M10 19h8"/></svg></h2>
    <p class="stage__text">we will present you with a detailed view of all shortlisted candidates, highlighting key strengths and potential development areas, as well as the results of the psychometric profile. We will then recommend the best candidates to meet with you.</p>
  </section>

  <section class="stage stage--right" style="top:441px">
    <div class="stage__number">6</div>
    <h2 class="stage__bar" style="margin:0;font-weight:400">Clients Interviews
      <svg class="stage__icon" viewBox="0 0 24 24" fill="#fff"><circle cx="5" cy="6" r="2.2"/><circle cx="19" cy="6" r="2.2"/><rect x="3" y="9" width="4" height="6"/><rect x="17" y="9" width="4" height="6"/><rect x="7" y="12" width="10" height="1.6"/><rect x="11.2" y="13" width="1.6" height="8"/><rect x="2" y="15" width="1.4" height="6"/><rect x="20.6" y="15" width="1.4" height="6"/></svg></h2>
    <p class="stage__text">we will arrange the interviews and can attend these with you if you wish. We offer an extended 12 month guarantee from our usual 6 month guarantee for a free of charge replacement if we participate in the interviews at this stage.<span>Our attendance can provide valuable competency interviewing experience as well as having a first-hand view of the interview performance, helping to provide suitable reasons for hiring or rejecting the candidate.</span></p>
  </section>

  <section class="stage stage--left" style="top:630px">
    <div class="stage__number">7</div>
    <h2 class="stage__bar" style="margin:0;font-weight:400">Offer and acceptance
      <svg class="stage__icon" viewBox="0 0 24 24" fill="none" stroke="#fff" stroke-width="1.6"><path d="M1 9l4-2 5 1 4-2 5 1 4 2M3 9l3 7 5 4 4-1 4-4 3-6M9 12l3 3M11 11l3 3M13 10l3 3"/></svg></h2>
    <p class="stage__text">we will act as the go-between for any offer to the successful candidate, negotiating on behalf of both parties when required.<span>We will also provide any unsuccessful candidates with constructive feedback as to why they were not successful. This ensures they are still left with a very positive impression of you (and us!). This can also significantly reduce the risk of a candidate's rejection being seen as discriminatory.</span></p>
  </section>

  <section class="stage stage--right" style="top:630px">
    <div class="stage__number">8</div>
    <h2 class="stage__bar" style="margin:0;font-weight:400">Follow-up
      <svg class="stage__icon" viewBox="0 0 24 24" fill="none" stroke="#fff" stroke-width="1.6"><rect x="7" y="9" width="15" height="11"/><path d="M7 9l7.5 6L22 9"/><path d="M3 3l3 1-1 3 2 3-2 1c-2-2-3-5-2-8z" fill="#fff"/></svg></h2>
    <p class="stage__text">we will keep in touch with the candidate prior to start date and guide them on handing in their notice and dealing with any counter-offers.<span>We will also follow-up with both you and the candidate after the candidate has started to make sure both parties are happy and the relationship is working well.</span></p>
  </section>

  <div class="page__footer-bar"></div>
</main>
</body>
</html>
```